Talvey Vineyards Plinkr website

We are opening a new winery called Talvey Vineyards. We think that "Wine should be an experience..." To aid in that experience, each bottle of wine label will have a unique QR code that directs patrons to a page on the site that highlights the wines. On this page each wine bottle will be displayed, the winemaking notes will be included. Also included will be food pairings with recipes, movie and music ideas and anything else that will add to the experience. I need a website that helps showcase annual wines, has a members only area (for the wine club) and allows people to purchase wine on-line. I've started the beginning of a site on Plinkr - talveyvineyards.example. There's no requirement or expectation to simply finish what I've started. I just needed to get something up and live. Let your imagination take over. I want to unique site and kicks a*s...

Logo font is Trajan Pro...

I'm open to any designs, meaning don't feel like you have to complete what I started.

I want to keep the logo and the font, however...

Other fonts used should compliment Trajan Pro.

Serif
• Trajan Pro is what was used for the logo

• Attractive and compelling home page, red wine section, white wine section, members only area, page that speaks of and allows purchase into a wine club, all easy enough for me to edit and add pages without coding knowledge. Adding pages is why I chose Plinkr as the platform. Here is a list of the pages or tabs: About, Events, Harvest Circle, Press/Accolades, Wines - Red/White/Dessert/Summer Series (as sub pages), Contact

```html
<!DOCTYPE html>
<html lang="en">
<head>
<meta charset="utf-8">
<title>Talvey Vineyards — Home and Wine Detail</title>
<link rel="stylesheet" href="https://fonts.googleapis.com/css2?family=Arimo:wght@700&family=Cinzel:wght@400;500&family=Cormorant+Garamond:ital,wght@0,400;0,500;1,500&family=EB+Garamond:ital,wght@0,400;0,500;1,400&display=swap">
<style>
:root{
  --ink:#000;
  --night:#0b0b0b;
  --paper:#fff;
  --gold:#a08a66;
  --gold-soft:#8d7a5c;
  --line:#c9c9c9;
  --rule-dark:#5b5142;
  --text-dark:#333;
  --text-light:#e8e8e8;
}
*{margin:0;padding:0;box-sizing:border-box}
html,body{width:1149px;height:1200px;overflow:hidden;background:var(--paper)}
body{position:relative;font-family:"EB Garamond",serif}
.abs{position:absolute}

/* ---------- shared nav ---------- */
.nav a{position:absolute;font-family:"Arimo",Arial,sans-serif;font-weight:700;font-size:7.4px;color:#fff;text-decoration:none;letter-spacing:.2px}
.brand-mark{position:absolute;font-family:"Cinzel",serif;font-weight:400;color:#fff;text-align:center;line-height:1.15}

/* ---------- home page ---------- */
.home{left:0;top:0;width:560px;height:1200px}
.hero{left:0;top:0;width:560px;height:381px;background:radial-gradient(ellipse at 40% 35%,#3a3a3a 0%,#1e1e1e 55%,#101010 100%)}
.hero-brand{left:130px;top:150px;width:165px;font-size:22px;letter-spacing:1px}
.hero-brand small{display:block;font-size:8px;letter-spacing:4px;margin-top:4px}
.tagline{left:52px;color:#fff;font-family:"Cormorant Garamond",serif;font-style:italic;font-weight:500}
.tagline.lead{top:243px;font-size:29px}
.tagline.big{top:281px;font-size:56px;letter-spacing:.5px}
.hero-bottles{left:367px;top:92px;width:172px;height:289px;background:linear-gradient(90deg,#151515,#3b3b3b 45%,#1a1a1a);border-radius:30px 30px 0 0}

.collection{left:0;top:381px;width:560px;height:273px;background:var(--paper);border:1px solid var(--line);border-top:none}
.collection h2{position:absolute;top:12px;width:100%;text-align:center;font-family:"Cinzel",serif;font-weight:400;font-size:14px;color:#222;letter-spacing:.5px}
.card{position:absolute;width:160px;height:82px}
.card .bottle{position:absolute;left:0;top:0;width:20px;height:81px;background:linear-gradient(90deg,#111,#3a2a2e 50%,#111);border-radius:6px 6px 3px 3px}
.card .cap-orange{background:linear-gradient(180deg,#f39a1e 0 13%,#161616 13%,#3a3a3a 60%,#111)}
.card .cap-green{background:linear-gradient(180deg,#5d9a6c 0 13%,#161616 13%,#3a3a3a 60%,#111)}
.card .cap-purple{background:linear-gradient(180deg,#5b3a78 0 13%,#161616 13%,#3a3a3a 60%,#111)}
.card h3{position:absolute;left:36px;top:30px;font-family:"Cinzel",serif;font-weight:400;font-size:7.2px;color:#222;letter-spacing:.3px}
.card .rule{position:absolute;left:36px;top:42px;width:95px;height:1px;background:#bbb}
.card p{position:absolute;left:36px;top:47px;width:110px;font-size:4.5px;line-height:6px;color:#555}
.card .price{position:absolute;left:39px;top:71px;font-size:7.2px;color:var(--gold)}
.card .cart{position:absolute;left:111px;top:71px;width:30px;height:8px;border:1px solid #555;font-family:"Arimo",Arial,sans-serif;font-weight:700;font-size:3.6px;line-height:6px;text-align:center;color:#333}
.arrow{position:absolute;top:515px}

.winemaker{left:0;top:654px;width:560px;height:273px;background:var(--ink)}
.winemaker-photo{left:0;top:0;width:332px;height:273px;background:radial-gradient(ellipse at 40% 40%,#8a8a8a 0%,#4a4a4a 45%,#000 80%)}
.message{left:329px;top:32px;width:205px;color:var(--text-light);font-size:9px;line-height:10.6px}
.message h4{font-weight:400;font-size:9px;letter-spacing:.2px;margin-bottom:11px}
.message p{margin-bottom:0}
.message .gap1{margin-top:23px}
.message .gap2{margin-top:24px}
.message .gap3{margin-top:10px}

.coming{left:0;top:927px;width:560px;height:273px;background:var(--ink)}
.coming-bottles{left:58px;top:20px;width:132px;height:213px;background:linear-gradient(90deg,#1a1a1a,#444 30%,#1c1c1c 50%,#444 75%,#1a1a1a);border-radius:18px 18px 6px 6px}
.coming-brand{left:340px;top:70px;width:90px;font-size:9px;color:var(--gold)}
.coming-brand small{display:block;font-size:4px;letter-spacing:2px}
.coming-text{left:225px;top:131px;width:320px;text-align:center;font-family:"Cormorant Garamond",serif;font-size:20px;line-height:24px;color:var(--gold)}

/* ---------- wine detail page ---------- */
.detail{left:590px;top:0;width:559px;height:412px;background:var(--ink)}
.detail-bottle{left:68px;top:86px;width:70px;height:275px;background:linear-gradient(180deg,#f39a1e 0 8%,#1b1b1b 8%,#2a2a2a 45%,#5a5a5a 55%,#2a2a2a 75%,#111);border-radius:26px 26px 8px 8px}
.detail h1{position:absolute;left:194px;top:80px;font-family:"Cinzel",serif;font-weight:500;font-size:18.5px;color:#fff;letter-spacing:.6px}
.detail .intro{position:absolute;left:194px;top:117px;width:210px;font-size:5.6px;line-height:7px;color:#ddd}
.detail .price{position:absolute;left:198px;top:147px;font-size:17px;color:var(--gold);font-weight:500}
.detail .note{position:absolute;left:197px;top:178px;width:170px;font-style:italic;font-size:5px;line-height:6.6px;color:#ccc}
.detail .hr{position:absolute;left:198px;width:325px;height:1px;background:var(--rule-dark)}
.specs{position:absolute;left:200px;top:218px;width:100px;font-size:6px;line-height:7.4px;color:#eee}
.specs dt{color:var(--gold-soft);margin-top:9.2px}
.specs dt:first-child{margin-top:0}
.specs dt.plain{color:#eee}
.notes{position:absolute;left:311px;top:216px;width:220px;font-size:6px;line-height:7.9px;color:#eee}
.notes h5{font-weight:500;font-size:9px;color:var(--gold);margin-bottom:6px}
.notes .label{color:var(--gold-soft);line-height:7px}
.notes .para{margin-top:8px}
.notes .food{margin-top:30px}
</style>
</head>
<body>

<!-- Home page -->
<section class="abs home">
  <header class="abs hero">
    <div class="brand-mark" style="left:24px;top:14px;width:40px;font-size:6px">TALVEY<br><span style="font-size:3px;letter-spacing:1px">VINEYARDS</span></div>
    <nav class="nav">
      <a style="left:190px;top:32px">HOME</a>
      <a style="left:257px;top:32px">ABOUT</a>
      <a style="left:324px;top:32px">EVENT</a>
      <a style="left:394px;top:32px">CONTACT</a>
      <a style="left:484px;top:32px">MEMBER</a>
    </nav>
    <div class="brand-mark hero-brand">TALVEY<small>VINEYARDS</small></div>
    <p class="abs tagline lead">Because wine should be an</p>
    <p class="abs tagline big">experience...</p>
    <div class="abs hero-bottles" role="img" aria-label="Three wine bottles with orange, green and purple caps"></div>
  </header>

  <section class="abs collection">
    <h2>Our Collection</h2>
    <article class="card" style="left:39px;top:38px">
      <div class="bottle" role="img" aria-label="Pinot Noir bottle"></div>
      <h3>Pinot Noir</h3><div class="rule"></div>
      <p>Served well-chilled our authentically made Cabernet Sauvignon is a refreshingly delicate dry wine with hints of strawberry, citrus, and peach laced fruit.</p>
    </article>
    <article class="card" style="left:215px;top:38px">
      <div class="bottle" role="img" aria-label="Tres Bella bottle"></div>
      <h3>Tres Bella</h3><div class="rule"></div>
      <p>Served well-chilled our authentically made Cabernet Sauvignon is a refreshingly delicate dry wine with hints of strawberry, citrus, and peach laced fruit.</p>
      <span class="price">$120.00</span><span class="cart">Add to Cart</span>
    </article>
    <article class="card" style="left:378px;top:38px">
      <div class="bottle" role="img" aria-label="Merlot Ruby Hills bottle"></div>
      <h3>Meriot Ruby Hils</h3><div class="rule"></div>
      <p>Served well-chilled our authentically made Cabernet Sauvignon is a refreshingly delicate dry wine with hints of strawberry, citrus, and peach laced fruit.</p>
      <span class="price">$120.00</span><span class="cart">Add to Cart</span>
    </article>
    <article class="card" style="left:39px;top:159px">
      <div class="bottle cap-orange" role="img" aria-label="Sauvignon Blanc bottle"></div>
      <h3>Sauvigon Blanc</h3><div class="rule"></div>
      <p>Served well-chilled our authentically made Cabernet Sauvignon is a refreshingly delicate dry wine with hints of strawberry, citrus, and peach laced fruit.</p>
      <span class="price">$120.00</span><span class="cart">Add to Cart</span>
    </article>
    <article class="card" style="left:215px;top:159px">
      <div class="bottle cap-green" role="img" aria-label="Pinot Grigio bottle"></div>
      <h3>Pinot Grigio</h3><div class="rule"></div>
      <p>Served well-chilled our authentically made Cabernet Sauvignon is a refreshingly delicate dry wine with hints of strawberry, citrus, and peach laced fruit.</p>
      <span class="price">$120.00</span><span class="cart">Add to Cart</span>
    </article>
    <article class="card" style="left:378px;top:159px">
      <div class="bottle cap-purple" role="img" aria-label="Malbec Columbia Gorge bottle"></div>
      <h3>Malec Columbia Gorge</h3><div class="rule"></div>
      <p>Served well-chilled our authentically made Cabernet Sauvignon is a refreshingly delicate dry wine with hints of strawberry, citrus, and peach laced fruit.</p>
      <span class="price">$120.00</span><span class="cart">Add to Cart</span>
    </article>
  </section>
  <svg class="arrow" style="left:10px" width="12" height="22" viewBox="0 0 12 22"><polyline points="11,1 1,11 11,21" fill="none" stroke="#999" stroke-width="0.8"/></svg>
  <svg class="arrow" style="left:537px" width="12" height="22" viewBox="0 0 12 22"><polyline points="1,1 11,11 1,21" fill="none" stroke="#999" stroke-width="0.8"/></svg>

  <section class="abs winemaker">
    <div class="abs winemaker-photo" role="img" aria-label="Black and white portrait of the winemaker tasting from a glass"></div>
    <div class="abs message">
      <h4>A MESSAGE FROM THE WINEMAKER</h4>
      <p>I started my winemaking journey with one simple goal in mind - I wanted to make wine as good or better than the wine I could buy.&nbsp; At the time of that goal in 2015, I had no perspective on the path that would form before me.</p>
      <p class="gap1">I'm excited for you to try my wine. Pair it with the food ideas. Follow the recipes; listen to the music.</p>
      <p class="gap2">Enjoy...the experience.</p>
      <p class="gap3">--Elliot Talvey</p>
    </div>
  </section>

  <section class="abs coming">
    <div class="abs coming-bottles" role="img" aria-label="Sauvignon Blanc, Pinot Grigio and Malbec bottles"></div>
    <div class="brand-mark coming-brand">TALVEY<small>VINEYARDS</small></div>
    <p class="abs coming-text">We are currently making and aging wines for a future launch. Please check back.</p>
  </section>
</section>

<!-- Wine detail page -->
<section class="abs detail">
  <div class="brand-mark" style="left:30px;top:16px;width:44px;font-size:6px">TALVEY<br><span style="font-size:3px;letter-spacing:1px">VINEYARDS</span></div>
  <nav class="nav">
    <a style="left:198px;top:34px">HOME</a>
    <a style="left:265px;top:34px">ABOUT</a>
    <a style="left:332px;top:34px">EVENT</a>
    <a style="left:402px;top:34px">CONTACT</a>
    <a style="left:491px;top:34px">MEMBER</a>
  </nav>
  <div class="abs detail-bottle" role="img" aria-label="Sauvignon Blanc 2024 bottle with orange cap"></div>
  <h1>SauvigNon Blanc</h1>
  <p class="intro">Served well-chilled our authentically made Cabernet Sauvignon is a refreshingly delicate dry wine with hints of strawberry, citrus, and peach laced fruit.</p>
  <p class="price">$120.00</p>
  <p class="note">This is an exclusive product that can only be purchased by member. To Purchase this product join one of Our Member plans or log in if you are already member</p>
  <div class="hr" style="top:211px"></div>
  <dl class="specs">
    <dt>VARIETAL</dt><dd>100% Cabernet Saufignon</dd>
    <dt>APPELLATION</dt><dd>Villenoir Cabernet Saufignon</dd>
    <dt>VINTAGE</dt><dd>2024</dd>
    <dt>Profile</dt><dd>Semi-dry</dd>
    <dt class="plain">ALCOHOL</dt><dd>13.5%</dd>
    <dt class="plain">VOLUME</dt><dd>750 mL; 850ml</dd>
  </dl>
  <div class="notes">
    <h5>Wine specs</h5>
    <p class="label">Tasting notes</p>
    <p>Deep garnet with a vibrant ruby edge, velvety soft on the palate with bright cherry to plum flavors. This wine is weighty and full of fresh ripe berries with rich, dark accents of cocoa nib. Intriguing and delicious. Aromas of dark chocolate, plum, black cherry, cedar and tarragon jump from the glass.</p>
    <p class="para">A potent perfumed mix of berries, fresh herbs and roasted notes with a bit a mineral. A compelling blend of fresh and bright aroma next the rich and dark.</p>
    <p class="label food">Food pairing notes</p>
    <p>One of our favorite blocks from the Villenoir vineyard. This block tends to lift the aromatic character and soften the palate of our Cabernet Sauvignon. We are proud to offer this very limited and barrel selected wine as a stand alone block.</p>
  </div>
  <div class="hr" style="top:370px"></div>
</section>

</body>
</html>
```